wardrobe/costume stylist needs good business card for own business

Hi:)

I'm wanting a business card for my company. I am a freelance stylist.

I do wardrobe/costume stylist to TV commercials; Films; Fashion and Lifestyle shoots.

I'd like a design based around my name Rosalind Pember written nicely, maybe a colour? Up to you?!

I've attached a couple of images of business cards I like
.... be creative and have fun!

Thank you :)
Updates

Reason: I was trying to get my new business card ready for before I headed overseas Friday morning but I don't think that was realistic so I'd like to extend the deadline to give time to the project. Thank you

Hi designers:) Thank you for all your designs, I've extended the deadline until Sunday, so there's a bit more time. I've attached 3 pictures of business cards which I quite like, please take a look to see if it can be of help in your process. I like the pale plain or patterned background with dark font and the dark plain or patterned background with the pale font the motifs the feminine fonts the plain fonts I like the idea of playing with a circle or some shape on one side of the card with my name or initials as in the picture I have on my post could you play around with this idea a bit please? Thank you all for the work you've done :) Rosa

Hi I am working overseas til Saturday night sorry for no feedback until I teturn Thanks :) Rosa

Hi designers, Thank you all so much for submitting your designs, I really appreciate your input into my project :) I'm sorry I didn't get to respond to some comments, and give feedback. I didn't back from being away until later than I expected, and the deadline had passed then, so apologies. Thanks to you all again for all your really good designs :) Rosa

Target Market(s)

I am a freelance stylist my target audience is producers, production companies, photographers, directors...

Industry/Entity Type

Business

Requirements
Must have
• Rosalind Pember
Stylist or Wardrobe Stylist

email rosapember@quillnet.co.nz
Mobile 0218846193

(Don't have to use the words 'email' and 'mobile')
Nice to have
• Would like it to be double sided
Like B & W
Like pale colour background with dark font or white font
Like dark colour background with pale font
Should not have
• I would prefer it not to incorporate pictures

```html
<!DOCTYPE html>
<html lang="en">
<head>
<meta charset="utf-8">
<title>Rosalind Pember — Wardrobe Stylist</title>
<link rel="stylesheet" href="https://fonts.googleapis.com/css2?family=Pirata+One&family=Oswald:wght@300;400;600&display=swap">
<style>
  :root {
    --card-brown: #4b2513;
    --card-brown-light: #5a2e18;
    --card-brown-dark: #3d1d0e;
    --ink-cream: #fbf7f2;
    --flourish-tone: rgba(255, 255, 255, 0.22);
  }
  html, body {
    margin: 0;
    padding: 0;
    width: 1200px;
    height: 702px;
    overflow: hidden;
    background: var(--card-brown-dark);
  }
  .business-card {
    position: relative;
    width: 1200px;
    height: 702px;
    overflow: hidden;
    background:
      radial-gradient(ellipse at 70% 40%, var(--card-brown-light) 0%, var(--card-brown) 55%, var(--card-brown-dark) 100%);
    color: var(--ink-cream);
  }
  .flourish-area {
    position: absolute;
    left: 0;
    top: 0;
    width: 490px;
    height: 702px;
    background: radial-gradient(ellipse at 20% 50%, var(--flourish-tone) 0%, rgba(255,255,255,0.08) 55%, rgba(255,255,255,0) 80%);
  }
  .stylist-name {
    position: absolute;
    left: 522px;
    top: 192px;
    margin: 0;
    font-family: "Pirata One", serif;
    font-weight: 400;
    font-size: 78px;
    line-height: 1;
    letter-spacing: 1px;
  }
  .stylist-role {
    position: absolute;
    left: 533px;
    top: 288px;
    margin: 0;
    font-family: "Oswald", sans-serif;
    font-weight: 300;
    font-size: 33px;
    line-height: 1;
    letter-spacing: 1.5px;
  }
  .contact-list {
    position: absolute;
    left: 522px;
    top: 362px;
    margin: 0;
    padding: 0;
    list-style: none;
  }
  .contact-row {
    display: flex;
    align-items: center;
    height: 62px;
    margin-bottom: 26px;
  }
  .contact-label {
    width: 103px;
    font-family: "Oswald", sans-serif;
    font-weight: 600;
    font-size: 58px;
    line-height: 1;
  }
  .contact-value {
    font-family: "Oswald", sans-serif;
    font-weight: 400;
    font-size: 42px;
    line-height: 1;
    letter-spacing: 1.2px;
  }
</style>
</head>
<body>
  <main class="business-card">
    <div class="flourish-area" role="img" aria-label="White swirling floral flourish ornament along the left edge"></div>

    <h1 class="stylist-name">Rosalind Pember</h1>
    <p class="stylist-role">WARDROBE STYLIST</p>

    <ul class="contact-list">
      <li class="contact-row">
        <span class="contact-label">M</span>
        <span class="contact-value">0218846193</span>
      </li>
      <li class="contact-row">
        <span class="contact-label">E</span>
        <span class="contact-value">rosapember@quillnet.co.nz</span>
      </li>
    </ul>
  </main>
</body>
</html>
```